Wealth Management Business Card

We are a professional services consulting firm that specializes in high net worth individuals over $25,000,000, executives C-suite and above, closely held businesses owners, family offices and highly compensated employees.

Our focus is on risk mitigation and tax efficient strategies. Our clients take their risk on themselves and have a proven track record generating wealth. Our directive is to preserve and protect the wealth they’ve already created.

Our company Harrowgate Advisory is geared around five directives of asset protection:
1) Legal Structuring
2) Leverage & Financing
3) Risk Management - Asset Protection & Insurance, Trustee Work
4) Asset Management & Investing - Under www.qlvbrookfield.com
5) Tax Efficient Strategies

Our Company Mark is a Pentagon with a key in the middle. A pentagon is the most efficient defensive structure. Each point of a pentagon is equal distance front every point . Each side provides support to another and works together, which is the key to our clients success.

Our key colors are blue, black and silver.

We ‘re located in the Pacific Northwest with bi coastal and international clients. We have fewer, higher net worth clients and provide exceptional customer service. We do not do social media.

website is www.harrowgatepath.com

Target Market(s)

High End Clients

Contact Information for Business Card

extra thick

Font styles to use
Serif

Requirements
Must have
• Metalic foil for lettering.
Black Background on one side
White Background on the other
Horizontal Format Only
No Rounded corners
Not Marketing sales information on the card.
Nice to have
• imprinted texture on the card
Should not have
• lots of color

```html
<!DOCTYPE html>
<html lang="en">
<head>
<meta charset="utf-8">
<title>Harrowgate Advisory – Business Card</title>
<link href="https://fonts.googleapis.com/css2?family=Cinzel:wght@500;600&family=Poppins:wght@400;500&display=swap" rel="stylesheet">
<style>
  :root {
    --stage: #e6e7e9;
    --card-black: #121213;
    --card-white: #ffffff;
    --navy: #1d3a78;
    --accent-blue: #1e8fd6;
    --silver: #d9dbde;
    --silver-dim: #a9adb3;
    --ink: #4a4d52;
    --serif: "Cinzel", "Times New Roman", serif;
    --sans: "Poppins", Arial, sans-serif;
  }
  * { box-sizing: border-box; margin: 0; padding: 0; }
  html, body { width: 1200px; height: 800px; overflow: hidden; }
  body {
    background: var(--stage);
    display: flex;
    align-items: center;
    justify-content: center;
    gap: 50px;
  }
  .card {
    position: relative;
    width: 525px;
    height: 300px;
    box-shadow: 0 10px 28px rgba(0,0,0,0.18);
    overflow: hidden;
  }

  /* Back side */
  .card--back { background: var(--card-black); }
  .back-brand {
    position: absolute;
    top: 92px;
    left: 0; right: 0;
    display: flex;
    align-items: center;
    justify-content: center;
    gap: 12px;
    font-family: var(--serif);
    font-weight: 600;
    font-size: 24px;
    letter-spacing: 3px;
    color: var(--silver);
    text-transform: uppercase;
  }
  .back-brand__square {
    width: 14px; height: 14px;
    background: var(--silver-dim);
  }
  .directives {
    position: absolute;
    left: 0; right: 0;
    bottom: 46px;
    list-style: none;
    font-family: var(--sans);
    font-size: 11.5px;
    color: var(--silver);
    text-align: center;
    line-height: 1.7;
  }
  .directives li { display: inline; }
  .directives li::before {
    content: "•";
    color: var(--accent-blue);
    margin: 0 5px 0 7px;
  }

  /* Front side */
  .card--front { background: var(--card-white); }
  .front-brand {
    position: absolute;
    top: 50px;
    right: 36px;
    font-family: var(--serif);
    font-weight: 600;
    font-size: 21px;
    letter-spacing: 1.5px;
    color: var(--navy);
    text-transform: uppercase;
  }
  .front-rule {
    position: absolute;
    top: 108px;
    left: 190px;
    right: 36px;
    height: 1px;
    background: var(--accent-blue);
  }
  .edge-mark {
    position: absolute;
    left: 0;
    top: 196px;
    width: 3px;
    height: 24px;
    background: var(--accent-blue);
  }
  .person {
    position: absolute;
    left: 38px;
    top: 158px;
    width: 250px;
  }
  .person__name {
    font-family: var(--serif);
    font-weight: 500;
    font-size: 18px;
    letter-spacing: 1px;
    color: var(--accent-blue);
    text-transform: uppercase;
    display: flex;
    align-items: flex-end;
    gap: 8px;
  }
  .person__name::after {
    content: "";
    flex: 1;
    height: 1px;
    background: var(--accent-blue);
    margin-bottom: 4px;
  }
  .person__role {
    font-family: var(--sans);
    font-size: 11px;
    color: var(--ink);
    margin-top: 2px;
  }
  .contact {
    position: absolute;
    left: 38px;
    top: 212px;
    list-style: none;
    font-family: var(--sans);
    font-size: 12px;
    color: var(--ink);
    line-height: 1.65;
  }
  .contact li { display: flex; align-items: center; gap: 8px; }
  .contact svg { width: 11px; height: 11px; fill: none; stroke: var(--navy); stroke-width: 1.6; }
  .address {
    position: absolute;
    left: 270px;
    top: 196px;
    font-family: var(--sans);
    font-style: normal;
    font-size: 12px;
    color: var(--ink);
    line-height: 1.55;
  }
</style>
</head>
<body>

  <section class="card card--back" aria-label="Card back">
    <div class="back-brand"><span class="back-brand__square"></span>Harrowgate Advisory</div>
    <ul class="directives">
      <li>Legal Structuring</li><li>Leverage &amp; Financing</li><li>Risk Management</li><br>
      <li>Asset Management &amp; Investing</li><li>Tax Efficient Strategies</li>
    </ul>
  </section>

  <section class="card card--front" aria-label="Card front">
    <div class="front-brand">Harrowgate Advisory</div>
    <div class="front-rule"></div>
    <div class="edge-mark"></div>

    <div class="person">
      <h1 class="person__name">Corwin Ashdale</h1>
      <p class="person__role">Founder</p>
    </div>

    <ul class="contact">
      <li>
        <svg viewBox="0 0 12 12"><rect x="3" y="1" width="6" height="10" rx="1"/><line x1="5" y1="9" x2="7" y2="9"/></svg>
        (503) 555-0142
      </li>
      <li>
        <svg viewBox="0 0 12 12"><rect x="1" y="2.5" width="10" height="7"/><polyline points="1,2.5 6,6.5 11,2.5"/></svg>
        info@harrowgatepath.com
      </li>
      <li>
        <svg viewBox="0 0 12 12"><circle cx="6" cy="6" r="5"/><ellipse cx="6" cy="6" rx="2.2" ry="5"/><line x1="1" y1="6" x2="11" y2="6"/></svg>
        www.harrowgatepath.com
      </li>
    </ul>

    <address class="address">
      418 Alder Bend Rd<br>
      Suite 112<br>
      Marlow Falls, OR 97099
    </address>
  </section>

</body>
</html>
```